Redesign of ademwolkhuis.nl – Clean, Trustworthy & User-Friendly Medical Equipment We...

PLEASE DO NOT CONTACT US OUTSIDE TEKENPLEIN.COM

We are looking for a talented and creative web designer to redesign the website www.ademwolkhuis.nl, a Dutch online store specializing in medical oxygen concentrators and related products.

The current website is functional but outdated in terms of design, structure, and user experience. We want a fresh, modern, and trustworthy design that reflects the medical and professional nature of the business, while also being clear, accessible, and easy to navigate for a broad audience — including elderly users and people with limited technical skills.

About the Business:
Ademwolkhuis.nl provides high-quality oxygen concentrators and accessories for both home and mobile use. The target audience includes individuals with respiratory conditions, healthcare professionals, and caregivers. Trust, clarity, and ease of use are key.

What We’re Looking For:
A clean and modern layout with a medical/professional feel
Strong focus on usability and accessibility
A design that works flawlessly on desktop and mobile (responsive)
Clear product presentation and easy-to-use navigation
Use of calming colors (e.g. white, light blue, grey tones) that reflect a medical/healthcare environment
Clear call-to-actions (e.g. “Vraag een offerte aan”, “Neem contact op”, etc.)
A design that builds trust and encourages inquiries or purchases

Pages We Need Designed:
Homepage
Product overview page (category)
Product detail page

Inspiration / Style Examples:
We’re looking for something in the style of:

Veltmar Careworks
Zorvan.nl
Welbrakkenshop.nl
Quint (for clean layout and spacing)

Deliverables:
Full desktop and mobile designs (Figma, Adobe PS)
All source files and assets used (fonts, icons, images, etc.)
Clean and organized layers
Design must be ready for implementation by our development team

Target Market(s)

Ademwolkhuis.nl targets both B2C and B2B audiences within the medical and healthcare sector in europe

Industry/Entity Type

Medical

Number of Pages Required

2 page

Font styles to use
Sans Serif

Requirements
Must have
• Clean and professional design, responsive layout (desktop and mobile), calming medical color scheme (e.g. light blue, white, grey), clear product presentation with specs and images, strong call-to-actions (e.g. "Vraag een offerte aan"), trust elements (certifications, reviews, support info), easy navigation for elderly and non-tech-savvy users, contact form easily accessible, SEO-friendly structure, fast loading design, privacy and regulatory compliance elements (e.g. CE mark info, medical disclaimers).
Should not have
• Overly complex design, dark or aggressive color schemes, small or hard-to-read fonts, cluttered layout, distracting animations, unnecessary pop-ups, autoplay videos or sounds, technical jargon without explanation, hidden contact options, slow-loading pages.

```html
<!DOCTYPE html>
<html lang="en">
<head>
<meta charset="utf-8">
<title>Aerna – Oxygen Concentrators</title>
<link href="https://fonts.googleapis.com/css2?family=Montserrat:wght@400;500;600;700&display=swap" rel="stylesheet">
<style>
:root{
  --blue:#12a3df;
  --ink:#3a3f4a;
  --text:#555b66;
  --muted:#8a8f98;
  --line:#e4e6ea;
  --soft:#f4f5f7;
  --footer:#3d4556;
  --white:#fff;
}
*{box-sizing:border-box;margin:0;padding:0}
html,body{width:1200px;height:2655px;overflow:hidden;background:var(--white)}
body{font-family:"Montserrat",sans-serif;color:var(--text);font-size:12px;position:relative}
.wrap{width:1050px;margin:0 auto;position:relative}
.sc{font-variant:small-caps}
svg{display:block}

/* top bar */
.topbar{height:35px;background:var(--soft);font-size:11px;color:var(--text)}
.topbar .wrap{display:flex;justify-content:space-between;align-items:center;height:35px}
.links{display:flex;white-space:nowrap}
.links span{padding:0 22px;border-left:1px solid var(--ink);line-height:14px}
.links span:first-child{padding-left:0;border:0}
.links.right span:last-child{padding-right:0}

/* header */
.header{height:75px}
.header .wrap{display:flex;align-items:center;height:75px}
.brand{font-size:34px;font-weight:700;color:var(--blue);display:flex;align-items:center;gap:8px;width:351px}
.brand i{width:14px;height:14px;background:var(--blue);border-radius:50%;display:block}
.search{display:flex;height:32px}
.search .cat{width:34px;background:var(--soft);font-size:11px;display:flex;align-items:center;justify-content:center}
.search .field{width:320px;background:var(--soft);margin-left:4px;font-size:11px;color:var(--muted);display:flex;align-items:center;padding-left:22px}
.search .btn{width:34px;background:var(--blue);display:flex;align-items:center;justify-content:center}
.lang{margin-left:10px;display:flex;align-items:center;gap:8px;font-size:11px}
.flag{width:34px;height:32px;background:var(--soft);display:flex;align-items:center;justify-content:center}
.flag b{width:18px;height:11px;background:#1f3f8f;display:block;border-top:4px solid #c8242f;border-bottom:4px solid #c8242f}
.cart{margin-left:auto;display:flex;align-items:center;gap:14px;font-size:11px;white-space:nowrap}
.cart .btn{width:34px;height:32px;background:var(--blue);display:flex;align-items:center;justify-content:center}

/* nav */
.nav{height:38px;background:var(--soft)}
.nav .wrap{display:flex;align-items:center;height:38px;font-size:11px}
.nav .items{display:flex;white-space:nowrap}
.nav .items span{padding:0 33px;border-left:1px solid var(--ink);line-height:16px}
.nav .items span:first-child{padding-left:0;border:0}
.nav .items span:last-child{padding-right:0}
.phone{margin-left:auto;flex:0 0 200px;height:38px;background:var(--blue);color:#fff;font-weight:700;font-size:12px;display:flex;align-items:center;justify-content:center;gap:8px}

/* hero */
.hero{margin-top:23px;height:542px;position:relative;
  background:
    radial-gradient(ellipse 260px 300px at 66% 38%,rgba(214,190,168,.75),transparent 70%),
    linear-gradient(100deg,#5f5d5a 0%,#7d7870 28%,#a99e90 50%,#c8b7a2 62%,#7e6f60 82%,#5b4e43 100%)}
.hero .wrap{padding-top:160px}
.hero h1{font-size:56px;color:#fff;font-weight:600;letter-spacing:1px;line-height:1}
.hero .cta{display:inline-block;margin-top:26px;background:var(--blue);color:#fff;font-weight:700;font-size:12px;padding:12px 37px}
.arrows{display:flex;gap:4px}
.arrows span{width:35px;height:31px;display:flex;align-items:center;justify-content:center;background:var(--soft)}
.arrows span.on{background:var(--blue)}
.hero .arrows{margin-top:70px}

/* features */
.features{margin-top:76px;display:flex}
.feature{flex:1;height:118px;display:flex;flex-direction:column;align-items:center;padding-top:14px;border-left:1px solid var(--line)}
.feature:first-child{border:0}
.feature .ico{width:63px;height:63px;border-radius:50%;background:var(--blue);display:flex;align-items:center;justify-content:center}
.feature p{margin-top:15px;font-size:16px;font-weight:500;color:var(--ink)}

/* intro */
.intro{margin-top:80px;text-align:center}
.intro h2{font-size:42px;font-weight:500;color:var(--ink)}
.intro .bar{width:70px;height:3px;background:var(--blue);margin:4px auto 0}
.intro p{width:730px;margin:26px auto 0;font-size:12px;line-height:19px}

/* sections */
.sec-head{display:flex;justify-content:space-between;align-items:center}
.sec-head h2{font-size:40px;font-weight:500;color:var(--ink)}
.products{margin-top:82px}
.cards{display:flex;gap:14px;margin-top:24px}
.card{width:252px;height:304px;box-shadow:0 2px 8px rgba(0,0,0,.08)}
.card .img{height:180px}
.card .body{padding:16px 22px}
.card h3{font-size:15px;font-weight:500;color:var(--ink)}
.price{margin-top:6px;font-size:13px}
.price b{color:var(--blue);font-weight:600;margin-right:12px}
.price s{color:var(--muted);text-decoration:none}
.acts{display:flex;gap:6px;margin-top:14px}
.acts span{width:35px;height:35px;border-radius:50%;background:var(--soft);display:flex;align-items:center;justify-content:center}

.brands{margin-top:92px}
.circles{display:flex;justify-content:space-between;margin-top:24px}
.circle{width:134px;height:134px;border-radius:50%;border:1.5px solid;display:flex;align-items:center;justify-content:center;font-weight:700;font-size:15px;box-shadow:0 6px 12px rgba(0,0,0,.08);text-align:center}
.divider{height:1px;background:var(--line);margin-top:52px}

.gallery{margin-top:86px}
.tiles{display:flex;gap:14px;margin-top:24px}
.tile{width:199px;height:170px;box-shadow:0 2px 8px rgba(0,0,0,.06);display:flex;align-items:center;justify-content:center}
.tile div{width:80px;height:112px;border-radius:8px}

/* footer */
.footer{position:absolute;left:0;right:0;top:2338px;height:317px;background:var(--footer);color:#fff}
.cols{display:flex;padding-top:62px}
.col h4{font-size:27px;font-weight:500;margin-bottom:4px;white-space:nowrap}
.col p{font-size:11.5px;line-height:22.5px}
.col:nth-child(1){width:245px}
.col:nth-child(2){width:334px}
.col:nth-child(3){width:257px}
.copy{position:absolute;left:75px;right:75px;top:270px;border-top:1px solid #8a91a0;text-align:center;font-size:11px;padding-top:16px}
.totop{position:absolute;right:26px;top:248px;width:40px;height:44px;background:var(--blue);display:flex;align-items:center;justify-content:center}
</style>
</head>
<body>

<div class="topbar"><div class="wrap">
  <div class="links"><span>Home</span><span>About Us</span><span>Contact Us</span><span>Delivery</span><span>Stock</span></div>
  <div class="links right"><span>Login</span><span>Register</span><span>Wishlist</span><span>Compare</span></div>
</div></div>

<header class="header"><div class="wrap">
  <div class="brand"><i></i>Aerna</div>
  <div class="search">
    <div class="cat">All</div>
    <div class="field">Search Here...</div>
    <div class="btn"><svg width="14" height="14" viewBox="0 0 14 14" fill="none" stroke="#fff" stroke-width="2"><circle cx="6" cy="6" r="4.5"/><path d="M9.5 9.5L13 13"/></svg></div>
  </div>
  <div class="lang"><div class="flag"><b></b></div>English
    <svg width="8" height="6" viewBox="0 0 8 6" fill="none" stroke="#555" stroke-width="1.5"><path d="M1 1l3 3 3-3"/></svg></div>
  <div class="cart">0 item(s) - €0.00
    <div class="btn"><svg width="16" height="16" viewBox="0 0 24 24" fill="#fff"><path d="M7 18a2 2 0 100 4 2 2 0 000-4zm10 0a2 2 0 100 4 2 2 0 000-4zM1 2h3.3l1 2H21l-3.6 8H8.1l-1 2H19v2H4l2.3-4.3L3 4H1z"/></svg></div>
  </div>
</div></header>

<nav class="nav"><div class="wrap">
  <div class="items"><span>All Categories</span><span>Oxygen Concentrator</span><span>Portable Oxygen Concentrator</span><span>Filters</span><span>Rental</span><span>Supplies</span></div>
  <div class="phone"><svg width="15" height="15" viewBox="0 0 24 24" fill="#fff"><path d="M6.6 10.8a15 15 0 006.6 6.6l2.2-2.2a1 1 0 011-.25 11.4 11.4 0 003.6.57 1 1 0 011 1V20a1 1 0 01-1 1A17 17 0 013 4a1 1 0 011-1h3.5a1 1 0 011 1c0 1.25.2 2.45.57 3.57a1 1 0 01-.25 1z"/></svg>0031-705551234</div>
</div></nav>

<section class="hero" role="img" aria-label="Photo of a young woman at home breathing through a nebulizer mask">
  <div class="wrap">
    <h1 class="sc">Breathwell 5</h1>
    <div class="cta">Veltmar Breathwell 5</div>
    <div class="arrows">
      <span><svg width="8" height="10" viewBox="0 0 8 10" fill="none" stroke="#333" stroke-width="1.6"><path d="M6 1L2 5l4 4"/></svg></span>
      <span class="on"><svg width="8" height="10" viewBox="0 0 8 10" fill="none" stroke="#fff" stroke-width="1.6"><path d="M2 1l4 4-4 4"/></svg></span>
    </div>
  </div>
</section>

<main class="wrap">
  <div class="features">
    <div class="feature"><div class="ico"><svg width="32" height="26" viewBox="0 0 32 26" fill="#fff"><rect x="2" y="4" width="18" height="14" rx="1"/><path d="M21 8h6l4 5v5h-10z"/><circle cx="8" cy="20" r="3"/><circle cx="25" cy="20" r="3"/></svg></div><p class="sc">Free Shipping</p></div>
    <div class="feature"><div class="ico"><svg width="28" height="26" viewBox="0 0 24 22" fill="#fff"><path d="M12 21l-1.5-1.3C5 15 2 12 2 7.5A5 5 0 0112 5a5 5 0 0110 2.5c0 4.5-3 7.5-8.5 12.2z"/></svg></div><p class="sc">Oxygen concentrator</p></div>
    <div class="feature"><div class="ico"><svg width="28" height="28" viewBox="0 0 24 24" fill="#fff"><path d="M7 18a2 2 0 100 4 2 2 0 000-4zm10 0a2 2 0 100 4 2 2 0 000-4zM1 2h3.3l1 2H21l-3.6 8H8.1l-1 2H19v2H4l2.3-4.3L3 4H1z"/></svg></div><p class="sc">Secure Shopping</p></div>
    <div class="feature"><div class="ico"><svg width="28" height="28" viewBox="0 0 24 24" fill="#fff"><path d="M6 2h12v3h4v3a5 5 0 01-5 5h-.5A5 5 0 0113 15.9V19h4v3H7v-3h4v-3.1A5 5 0 017.5 13H7a5 5 0 01-5-5V5h4zm-2 5v1a3 3 0 002 2.8V7zm16 0h-2v3.8A3 3 0 0020 8z"/></svg></div><p class="sc">22 years experience</p></div>
  </div>

  <section class="intro">
    <h2 class="sc">Aerna BV Oxygen concentrator</h2>
    <div class="bar"></div>
    <p>Aerna BV was founded in 2003 and has a premium range of oxygen concentrators. We have the largest online offers for the Netherlands and Belgium.Whether you are looking for a fixed oxygen concentrator or a portable / portable / mobile oxygen concentrator. We make the difference in knowledge, service and low prices.</p>
  </section>

  <section class="products">
    <div class="sec-head"><h2 class="sc">Our Products</h2>
      <div class="arrows"><span><svg width="8" height="10" viewBox="0 0 8 10" fill="none" stroke="#333" stroke-width="1.6"><path d="M6 1L2 5l4 4"/></svg></span><span class="on"><svg width="8" height="10" viewBox="0 0 8 10" fill="none" stroke="#fff" stroke-width="1.6"><path d="M2 1l4 4-4 4"/></svg></span></div>
    </div>
    <div class="cards">
      <article class="card"><div class="img" role="img" aria-label="Woman seated on a green sofa with an oxygen mask" style="background:radial-gradient(ellipse 90px 80px at 55% 45%,rgba(222,205,180,.8),transparent 75%),linear-gradient(180deg,#d69a5c 0%,#c98a4e 45%,#6f7545 100%)"></div>
        <div class="body"><h3 class="sc">Evenstream oxygen...</h3><div class="price"><b>€790.25</b><s>€900.00</s></div>
        <div class="acts"><span><svg width="12" height="11" viewBox="0 0 24 22" fill="#12a3df"><path d="M12 21l-1.5-1.3C5 15 2 12 2 7.5A5 5 0 0112 5a5 5 0 0110 2.5c0 4.5-3 7.5-8.5 12.2z"/></svg></span><span><svg width="12" height="12" viewBox="0 0 24 24" fill="#12a3df"><path d="M7 18a2 2 0 100 4 2 2 0 000-4zm10 0a2 2 0 100 4 2 2 0 000-4zM1 2h3.3l1 2H21l-3.6 8H8.1l-1 2H19v2H4l2.3-4.3L3 4H1z"/></svg></span></div></div></article>
      <article class="card"><div class="img" role="img" aria-label="Metal gas valve with pressure gauge" style="background:radial-gradient(circle 40px at 52% 40%,#e8e9ea,transparent 80%),linear-gradient(90deg,#8d8f90 0%,#c9cacb 30%,#a3a5a6 60%,#d2d3d4 80%,#6f7172 100%)"></div>
        <div class="body"><h3 class="sc">Flamguard valve</h3><div class="price"><b>€9.95</b></div>
        <div class="acts"><span><svg width="12" height="11" viewBox="0 0 24 22" fill="#12a3df"><path d="M12 21l-1.5-1.3C5 15 2 12 2 7.5A5 5 0 0112 5a5 5 0 0110 2.5c0 4.5-3 7.5-8.5 12.2z"/></svg></span><span><svg width="12" height="12" viewBox="0 0 24 24" fill="#12a3df"><path d="M7 18a2 2 0 100 4 2 2 0 000-4zm10 0a2 2 0 100 4 2 2 0 000-4zM1 2h3.3l1 2H21l-3.6 8H8.1l-1 2H19v2H4l2.3-4.3L3 4H1z"/></svg></span></div></div></article>
      <article class="card"><div class="img" role="img" aria-label="Compact nebulizer unit with a clear mask" style="background:radial-gradient(ellipse 70px 55px at 55% 62%,rgba(120,190,205,.7),transparent 75%),linear-gradient(180deg,#4a4c4f 0%,#8c8f92 35%,#cfd1d3 75%,#9fa3a6 100%)"></div>
        <div class="body"><h3 class="sc">Oxygen concentrator...</h3><div class="price"><b>€801.15</b><s>€699.25</s></div>
        <div class="acts"><span><svg width="12" height="11" viewBox="0 0 24 22" fill="#12a3df"><path d="M12 21l-1.5-1.3C5 15 2 12 2 7.5A5 5 0 0112 5a5 5 0 0110 2.5c0 4.5-3 7.5-8.5 12.2z"/></svg></span><span><svg width="12" height="12" viewBox="0 0 24 24" fill="#12a3df"><path d="M7 18a2 2 0 100 4 2 2 0 000-4zm10 0a2 2 0 100 4 2 2 0 000-4zM1 2h3.3l1 2H21l-3.6 8H8.1l-1 2H19v2H4l2.3-4.3L3 4H1z"/></svg></span></div></div></article>
      <article class="card"><div class="img" role="img" aria-label="Patient in a hospital bed wearing an oxygen mask" style="background:radial-gradient(ellipse 80px 60px at 62% 40%,rgba(190,215,205,.8),transparent 75%),linear-gradient(135deg,#eef0f3 0%,#d7dde4 50%,#b3bdc8 100%)"></div>
        <div class="body"><h3 class="sc">Oxygen mask with 2.1...</h3><div class="price"><b>€2.18</b><s>€2.78</s></div>
        <div class="acts"><span><svg width="12" height="11" viewBox="0 0 24 22" fill="#12a3df"><path d="M12 21l-1.5-1.3C5 15 2 12 2 7.5A5 5 0 0112 5a5 5 0 0110 2.5c0 4.5-3 7.5-8.5 12.2z"/></svg></span><span><svg width="12" height="12" viewBox="0 0 24 24" fill="#12a3df"><path d="M7 18a2 2 0 100 4 2 2 0 000-4zm10 0a2 2 0 100 4 2 2 0 000-4zM1 2h3.3l1 2H21l-3.6 8H8.1l-1 2H19v2H4l2.3-4.3L3 4H1z"/></svg></span></div></div></article>
    </div>
  </section>

  <section class="brands">
    <div class="sec-head"><h2 class="sc">Shop by Brand</h2>
      <div class="arrows"><span><svg width="8" height="10" viewBox="0 0 8 10" fill="none" stroke="#333" stroke-width="1.6"><path d="M6 1L2 5l4 4"/></svg></span><span class="on"><svg width="8" height="10" viewBox="0 0 8 10" fill="none" stroke="#fff" stroke-width="1.6"><path d="M2 1l4 4-4 4"/></svg></span></div>
    </div>
    <div class="circles">
      <div class="circle" style="border-color:#e32b2b;color:#e32b2b">Gasvoro</div>
      <div class="circle" style="border-color:#3552d8;color:#3552d8">Invelta</div>
      <div class="circle" style="border-color:#f07a2a;color:#f07a2a">Aerna</div>
      <div class="circle" style="border-color:#2a5ea8;color:#2a5ea8">Nogaro</div>
      <div class="circle" style="border-color:#333;color:#2a4aa0;font-size:13px">Veltmar<br>Respira</div>
      <div class="circle" style="border-color:#1d6fb8;color:#1d6fb8">Corvane</div>
      <div class="circle" style="border-color:#f0b43a;color:#2a3a7a">Dovanis</div>
    </div>
    <div class="divider"></div>
  </section>

  <section class="gallery">
    <div class="sec-head"><h2 class="sc">Our Gallery</h2>
      <div class="arrows"><span><svg width="8" height="10" viewBox="0 0 8 10" fill="none" stroke="#333" stroke-width="1.6"><path d="M6 1L2 5l4 4"/></svg></span><span class="on"><svg width="8" height="10" viewBox="0 0 8 10" fill="none" stroke="#fff" stroke-width="1.6"><path d="M2 1l4 4-4 4"/></svg></span></div>
    </div>
    <div class="tiles">
      <div class="tile"><div role="img" aria-label="Dark stationary oxygen concentrator" style="background:linear-gradient(135deg,#3a3c41,#1f2024)"></div></div>
      <div class="tile"><div role="img" aria-label="Light blue oxygen concentrator" style="background:linear-gradient(135deg,#8ebde4,#5e95c6)"></div></div>
      <div class="tile"><div role="img" aria-label="Grey portable concentrator on a trolley" style="background:linear-gradient(135deg,#5a5e64,#373a3f)"></div></div>
      <div class="tile"><div role="img" aria-label="White compact portable concentrator" style="background:linear-gradient(135deg,#f4f6f9,#d5dbe3)"></div></div>
      <div class="tile"><div role="img" aria-label="White and blue concentrator on wheels" style="background:linear-gradient(90deg,#3b7fd0 22%,#eceef1 22%,#dfe2e6 100%)"></div></div>
    </div>
  </section>
</main>

<footer class="footer">
  <div class="wrap">
    <div class="cols">
      <div class="col"><h4 class="sc">About us</h4><p>About us</p><p>Dispatch</p><p>Privacy Policy</p><p>General terms and conditions</p><p>Commercial</p></div>
      <div class="col"><h4 class="sc">Customer service</h4><p>Contact</p><p>Warranty and Service</p><p>Returns</p><p>Site Map</p><p>To notice</p></div>
      <div class="col"><h4 class="sc">My account</h4><p>My account</p><p>Order history</p></div>
      <div class="col"><h4 class="sc">Documentation</h4><p>Frequently Asked Questions</p></div>
    </div>
  </div>
  <div class="copy">Copyright © 2003-2025, Aerna BV, All Rights Reserved</div>
  <div class="totop"><svg width="12" height="8" viewBox="0 0 12 8" fill="none" stroke="#fff" stroke-width="1.8"><path d="M1 7l5-5 5 5"/></svg></div>
</footer>

</body>
</html>
```